Cafe / catering Flyer

We are a higher end Industrial Cafe, located between factorys across from the postoffice in Campbellfield. I would like the following information on my flyer

Halvering Grove Cafe
Address: 14 Brindock St, Campbellfield 3061 (Across from Post Office)
Ph: 9472 6185
Email:halgrovecafe@mailbrook.net
Like us on Chatterbook: Halvering Grove Cafe
Download our App: Halvering Grove Cafe
Trading hours: Mon to Fri 5:30am to 4pm And Sat 7am to 1pm.
Amazing Breakfast Menu and even better Lunch menu!! Eat in or Takeaway
Daily CHEF made meals, Foccacias and wraps, fresh sandwich bar and fresh salads.
Best cafe in Campbellfield!!
Free local deliveries for orders over $50.
Daily Milk and paper deliveries to offices in the local area.
Free WIFI

The main purpose of the flyer is to pick up new big corporate customers that will hopefully take advantage of our catering services delivered to their office. I want to see a big emphasis made on the following :

CATERING CATERING CATERING!!
Delicious Fresh food delivered straight to your office. We cater for any function, or meeting. No Job too big or too Small

We offer a massive range from simple platters to a full ROAST BUFFET.
We Guarantee to impress
20% OFF FOR FIRST TIME CATERING CUSTOMERS!!
Contact us today to see what we can do for you.

Target Market(s)

corporate customers in the local area.

Industry/Entity Type

Cafe

Requirements
Must have
• Must have a big emphasis on Catering. I would like to pick up customers fro this side of the business
Nice to have
• dot points
• straight to the point
Should not have
• too much writing

```html
<!DOCTYPE html>
<html lang="en">
<head>
<meta charset="utf-8">
<title>Halvering Grove Cafe – Flyer</title>
<link href="https://fonts.googleapis.com/css2?family=Oswald:wght@300;400;500;600&display=swap" rel="stylesheet">
<style>
:root{
  --orange:#f7941d;
  --black:#0d0d0d;
  --ink:#111111;
  --white:#ffffff;
  --soft-white:#e8e8e8;
  --canvas:#e9e6e1;
}
*{box-sizing:border-box;margin:0;padding:0}
html,body{width:1200px;height:1058px;overflow:hidden;background:var(--canvas)}
body{position:relative;font-family:"Oswald",sans-serif;text-transform:uppercase}
.flyer{position:absolute;left:250px;width:700px;height:495px;overflow:hidden;background:var(--black);color:var(--white);box-shadow:0 4px 16px rgba(0,0,0,.25)}
.flyer--front{top:23px}
.flyer--back{top:540px}
.top-strip{position:absolute;left:0;top:0;width:100%;height:10px;background:var(--orange)}

/* brand */
.brand{position:absolute;display:flex;flex-direction:column;align-items:center;width:130px}
.brand__circle{width:96px;height:96px;border-radius:50%;border:6px solid var(--orange)}
.brand__rule{width:120px;height:3px;background:var(--orange);margin:14px 0 6px}
.brand__name{font-weight:600;font-size:14px;line-height:1.1;text-align:center;color:var(--white);width:130px}

/* photos */
.photo{position:absolute;border-radius:50%;border:2px solid var(--orange)}
.photo--salad{left:200px;top:176px;width:86px;height:86px;background:radial-gradient(circle at 40% 40%,#7fae4a,#3d5f2a 60%,#b33b2a)}
.photo--coffee{left:266px;top:262px;width:80px;height:80px;background:radial-gradient(circle at 50% 50%,#a9734a,#efe8df 55%,#7d7770)}
.photo--muffins{left:296px;top:340px;width:76px;height:76px;background:radial-gradient(circle at 45% 45%,#c4662c,#6b3a1f 65%,#2c2420)}
.photo--toast{left:22px;top:232px;width:262px;height:292px;border:4px solid var(--orange);background:radial-gradient(ellipse at 45% 45%,#f3f0e6 10%,#8fb24d 35%,#c48a4e 60%,#e9e4da 80%)}
.photo--lasagne{left:565px;top:178px;width:104px;height:104px;background:radial-gradient(circle at 50% 50%,#e6b84a,#b64a26 60%,#3a2a1e)}
.photo--chicken{left:490px;top:270px;width:100px;height:100px;background:radial-gradient(circle at 50% 50%,#b5532a,#6e2a16 60%,#2a1a14)}

/* front copy */
.headline{position:absolute;right:22px;top:26px;text-align:right;font-weight:300;font-size:36px;line-height:1.08;letter-spacing:.3px}
.headline__sub{display:block;font-size:16px;margin-top:4px;letter-spacing:.5px}
.front-rule{position:absolute;left:300px;right:22px;top:150px;height:4px;background:var(--orange)}
.offer-list{position:absolute;right:22px;top:162px;width:340px;text-align:right;font-weight:300;font-size:14px;line-height:1.5;list-style:none}
.badge{display:inline-block;background:var(--orange);color:var(--ink);font-weight:500;font-size:16px;line-height:1.4;padding:0 10px;border-radius:14px;margin:3px 0}

/* bottom bands */
.band{position:absolute;left:0;width:100%;background:var(--orange);color:var(--ink)}
.front-band{top:408px;height:74px}
.back-band{top:398px;height:84px}
.band-line{position:absolute;left:0;width:100%;height:3px;background:var(--orange)}
.footer-strip{position:absolute;left:0;bottom:0;width:100%;height:13px;background:var(--black);font-size:7px;line-height:13px;color:var(--white);display:flex;justify-content:space-between;padding:0 20px}
.hours{position:absolute;left:298px;top:10px;font-size:12.5px;line-height:1.45}
.divider{position:absolute;top:8px;bottom:8px;width:2px;background:var(--black)}
.divider--front{left:440px}
.divider--back{left:395px}
.contact{position:absolute;right:18px;top:8px;text-align:right;font-size:11.5px;line-height:1.35;white-space:nowrap}
.contact small{font-size:9px;display:block}
.contact--back{top:8px;font-size:14px}
.contact--back small{font-size:11px}
.contact__email{font-size:11px}

/* back copy */
.back-scene{position:absolute;inset:0;background:linear-gradient(180deg,#3c3c3c 0%,#2a2a2a 45%,#323232 100%)}
.brand-box{position:absolute;right:0;top:10px;width:175px;height:175px;background:var(--black)}
.catering{position:absolute;left:22px;top:50px;width:480px}
.catering__title{font-weight:500;font-size:33px;letter-spacing:.5px}
.catering__lines{font-weight:300;font-size:19px;line-height:1.45;color:var(--soft-white)}
.range{position:absolute;left:22px;top:215px;font-weight:300;font-size:32px;line-height:1.3}
.guarantee{position:absolute;left:22px;top:322px;font-weight:300;font-size:19px;color:var(--soft-white)}
.discount{position:absolute;left:22px;top:350px;font-weight:500;font-size:22px}
.cta{position:absolute;left:20px;top:6px}
.cta__title{font-weight:500;font-size:34px;line-height:1.15}
.cta__sub{font-size:19px}
</style>
</head>
<body>

<section class="flyer flyer--front">
  <div class="top-strip"></div>

  <div class="brand" style="left:18px;top:36px">
    <div class="brand__circle"></div>
    <div class="brand__rule"></div>
    <div class="brand__name">Halvering Grove Cafe</div>
  </div>

  <h1 class="headline">Amazing breakfast menu<br>and even better lunch menu!<span class="headline__sub">Eat in or takeaway</span></h1>
  <div class="front-rule"></div>

  <div class="photo photo--salad" role="img" aria-label="Photo of a fresh salad bar"></div>
  <div class="photo photo--coffee" role="img" aria-label="Photo of cups of coffee"></div>
  <div class="photo photo--muffins" role="img" aria-label="Photo of baked muffins"></div>

  <ul class="offer-list">
    <li>Daily chef made meals,</li>
    <li>Foccacias and wraps,</li>
    <li>Fresh sandwich bar and</li>
    <li>Fresh salads.</li>
    <li><span class="badge">Best cafe in Campbellfield!</span></li>
    <li>Free local deliveries for orders over $50.</li>
    <li>Daily milk and paper deliveries to offices</li>
    <li>in the local area.</li>
    <li>Free WiFi</li>
  </ul>

  <div class="band front-band">
    <div class="hours">Trading hours:<br>Mon to Fri: 5:30am to 4pm<br>Sat: 7am to 1pm.</div>
    <div class="divider divider--front"></div>
    <div class="contact">Address: 14 Brindock St, Campbellfield 3061<small>(Across from post office)</small>Ph: 9472 6185<br>Email: halgrovecafe@mailbrook.net</div>
  </div>
  <div class="footer-strip"><span style="margin-left:270px">Like us on Chatterbook: Halvering Grove Cafe</span><span>Download our app: Halvering Grove Cafe</span></div>

  <div class="photo photo--toast" role="img" aria-label="Photo of smashed avocado toast with poached egg"></div>
</section>

<section class="flyer flyer--back">
  <div class="back-scene" role="img" aria-label="Darkened photo of the cafe shopfront"></div>
  <div class="top-strip"></div>

  <div class="brand-box">
    <div class="brand" style="left:22px;top:12px">
      <div class="brand__circle"></div>
      <div class="brand__rule"></div>
      <div class="brand__name">Halvering Grove Cafe</div>
    </div>
  </div>

  <div class="catering">
    <h2 class="catering__title">Catering catering catering!!</h2>
    <p class="catering__lines">Delicious fresh food delivered straight to your office.<br>We cater for any function, or meeting.<br>No job too big or too small</p>
  </div>

  <p class="range">We offer a massive range from simple<br>platters to a full roast buffet.</p>
  <p class="guarantee">We guarantee to impress</p>
  <p class="discount">20% off for first time catering customers!!</p>

  <div class="photo photo--lasagne" role="img" aria-label="Photo of a lasagne serving"></div>
  <div class="photo photo--chicken" role="img" aria-label="Photo of a tray of roast chicken"></div>

  <div class="band-line" style="top:393px"></div>
  <div class="band back-band">
    <div class="cta">
      <div class="cta__title">Contact us today</div>
      <div class="cta__sub">To see what we can do for you.</div>
    </div>
    <div class="divider divider--back"></div>
    <div class="contact contact--back">Address: 14 Brindock St, Campbellfield 3061<small>(Across from post office)</small>Ph: 9472 6185<br><span class="contact__email">Email: halgrovecafe@mailbrook.net</span></div>
  </div>
  <div class="footer-strip"><span style="margin-left:170px">Like us on Chatterbook: Halvering Grove Cafe</span><span>Download our app: Halvering Grove Cafe</span></div>
</section>

</body>
</html>
```